Start-up consultancy in Healthcare Space requiring clean and crisp website design

I am the founder of a start-up consultancy to improve access to medicines and healthcare around the globe. My primary product are consulting services to both the public sector and the private sector to work on: improved healthcare delivery, the right price for medicines and addressing challenges in emerging markets. As the sector is fairly conservative, I need a clean and very professional website as is should signal competence in the sector. Therefore, I like shades of white and green but there should be a link to healthcare. Please see the logo that is featured on my business cards.

Target Market(s)

Ministry of Health, Pharmaceutical companies, Emerging Markets (Latin America, Middle East, Eastern Europe, Asia)

Industry/Entity Type

Healthcare

Coding

Coded - Design and coding required

Number of Pages Required

5+ page

Font styles to use
Serif

Colors

Designer to choose colors to be used in the design.

Requirements
Must have
• About Section
• Services Section
• Blog Section
• The website design should also portray the solution for access to healthcare and highlight my ability to help clients with that.
• The website will be hosted on a CMS and should therefore be easy to adjust. I would prefer wordpress but open to any suggestions as I have my own webspace.
• I quite like these websites:
• https://www.velmorhub.com/why-tandri
• https://home.quillstonecare.com/
Nice to have
• I like to see some creative thinking with the theme of healthcare.
Should not have
• The design should not feature too many hospitals or pills etc. as this is really not my focus.

```html
<!DOCTYPE html>
<html lang="en">
<head>
<meta charset="utf-8">
<title>Veldran Consulting</title>
<link href="https://fonts.googleapis.com/css2?family=Raleway:wght@400;600;700;800&family=Open+Sans:wght@400;600;700&display=swap" rel="stylesheet">
<style>
:root{
  --green:#0b6b3a;
  --green-dark:#08552e;
  --orange:#f28c1c;
  --ink:#2a2e33;
  --muted:#7a8088;
  --line:#dfe3e7;
  --pale:#eef1f4;
  --dark:#22262a;
  --darker:#1b1e21;
  --white:#ffffff;
}
*{margin:0;padding:0;box-sizing:border-box}
html,body{width:1200px;height:3468px;overflow:hidden}
body{font-family:"Open Sans",Arial,sans-serif;color:var(--ink);background:var(--white);position:relative;font-size:12px;line-height:1.6}
.abs{position:absolute}
h1,h2,h3,h4,.nav a,.btn,.label{font-family:"Raleway",Arial,sans-serif}

/* top bar + header */
.topbar{left:0;top:0;width:1200px;height:22px;background:var(--dark);color:#cfd3d6;font-size:10px;text-align:right;padding:4px 160px 0}
.header{left:0;top:22px;width:1200px;height:66px;background:var(--white);border-bottom:1px solid var(--line)}
.logo{left:160px;top:14px;display:flex;align-items:center;gap:8px}
.logo .mark{width:14px;height:14px;background:var(--green)}
.logo .name{font-family:"Raleway",sans-serif;font-weight:700;font-size:18px;color:var(--ink);letter-spacing:1px;line-height:1}
.logo .sub{font-family:"Raleway",sans-serif;font-weight:700;font-size:9px;color:var(--ink);letter-spacing:2px;display:block;margin-top:3px}
.nav{right:160px;top:26px;display:flex;gap:30px}
.nav a{font-size:10px;font-weight:700;color:var(--ink);text-decoration:none;letter-spacing:1px}
.nav a.active{color:var(--green)}

/* hero */
.hero{left:0;top:88px;width:1200px;height:560px;background:linear-gradient(120deg,#8a8f93 0%,#c9bfa6 35%,#b7a887 55%,#6f7b86 80%,#3f4a55 100%)}
.hero-shade{left:0;top:88px;width:1200px;height:560px;background:rgba(20,25,30,.35)}
.hero-kicker{left:0;top:262px;width:1200px;text-align:center;color:var(--white);font-family:"Raleway",sans-serif;font-weight:600;font-size:18px;letter-spacing:2px}
.hero-title{left:0;top:288px;width:1200px;text-align:center;color:#ffd34d;font-size:46px;font-weight:800;letter-spacing:1px}
.btn{display:inline-block;background:var(--green);color:var(--white);font-size:10px;font-weight:700;letter-spacing:1px;padding:9px 20px;text-decoration:none}
.hero-btn{left:545px;top:370px}
.newsletter{left:160px;top:584px;width:880px;height:34px;background:rgba(30,34,38,.85);display:flex;align-items:center;padding:0 12px;gap:14px}
.newsletter .nl-label{color:var(--white);font-family:"Raleway",sans-serif;font-weight:800;font-size:15px;display:flex;align-items:center;gap:8px;width:200px}
.newsletter .nl-label small{display:block;font-size:8px;font-weight:600;color:#cfd3d6;letter-spacing:1px}
.nl-icon{width:22px;height:22px;background:var(--orange)}
.nl-input{width:230px;height:22px;background:var(--white);font-size:9px;color:var(--muted);padding:4px 8px}
.nl-btn{background:var(--orange);color:var(--white);font-size:10px;font-weight:700;padding:5px 22px;font-family:"Raleway",sans-serif}

/* section headings */
.sec-head{left:0;width:1200px;text-align:center}
.sec-head .tag{display:inline-block;background:var(--green);color:var(--white);font-size:8px;font-weight:700;padding:1px 8px;letter-spacing:1px}
.sec-head h2{font-size:20px;font-weight:800;letter-spacing:1px;margin-top:4px}
.sec-head.light h2{color:var(--white)}
.sec-head.light .tag{background:var(--white);color:var(--green)}

/* about */
.about-img{left:200px;top:788px;width:300px;height:132px;background:linear-gradient(135deg,#c8d3dc,#8497a8 60%,#4d5f70)}
.about-text{left:540px;top:778px;width:470px;font-size:11px;color:var(--muted);line-height:1.75}
.about-btn{left:540px;top:954px}

/* services */
.services{left:0;top:1060px;width:1200px;height:420px;background:var(--pale)}
.svc{width:270px;display:flex;gap:14px}
.svc .ic{width:44px;height:44px;border:1px solid #c7ccd1;flex:none;display:flex;align-items:center;justify-content:center;background:var(--white)}
.svc .ic.on{background:var(--green);border-color:var(--green)}
.svc h4{font-size:14px;font-weight:600;color:var(--ink)}
.svc p{font-size:10px;color:var(--muted);line-height:1.6}

/* clients */
.clients{left:0;top:1512px;width:1200px;height:460px;background:var(--green)}
.quote-ic{left:582px;top:1656px;width:36px;height:36px;border-radius:50%;border:2px solid var(--white)}
.quote{left:260px;top:1712px;width:680px;text-align:center;color:var(--white);font-size:11px;line-height:1.8}
.by{left:0;top:1786px;width:1200px;text-align:center;color:var(--white);font-size:9px}
.by b{display:block;font-size:10px;letter-spacing:1px}
.avatar{left:572px;top:1828px;width:56px;height:56px;border-radius:50%;background:linear-gradient(135deg,#b0443a,#6c2521);border:3px solid var(--white)}
.dots{left:0;top:1914px;width:1200px;display:flex;justify-content:center;gap:6px}
.dots span{width:7px;height:7px;border-radius:50%;background:rgba(255,255,255,.5)}
.dots span.on{background:var(--white)}

/* team */
.team{left:0;top:2000px;width:1200px;height:468px;background:var(--pale)}
.member{top:2132px;width:196px;height:308px;background:var(--white)}
.member .photo{width:196px;height:212px;background:linear-gradient(160deg,#e6e9ec,#a9b3bc 55%,#3a434c)}
.member .cap{padding:18px 16px;font-size:9px}
.member .cap b{display:block;font-size:10px;color:var(--ink);letter-spacing:.5px}
.member .cap span{color:var(--orange)}
.member.featured{background:var(--green-dark)}
.member.featured .cap b{color:var(--white)}

/* blog */
.blog-img{left:172px;top:2600px;width:848px;height:330px;background:linear-gradient(120deg,#f1efe9,#d9d4c8 40%,#a9afb5 75%,#7b8791)}
.date{left:172px;top:2600px;width:46px;height:52px;background:var(--green);color:var(--white);text-align:center;font-family:"Raleway",sans-serif;padding-top:6px}
.date b{display:block;font-size:20px;line-height:1}
.date span{font-size:8px;letter-spacing:1px}
.blog-title{left:172px;top:2968px;font-size:14px;font-weight:700}
.blog-meta{right:180px;top:2972px;font-size:9px;color:var(--muted);display:flex;gap:22px}
.blog-text{left:172px;top:2998px;width:848px;font-size:10px;color:var(--muted);line-height:1.7}
.blog-btn{left:172px;top:3100px}

/* footer */
.footer{left:0;top:3188px;width:1200px;height:280px;background:var(--dark);color:#a8adb2}
.footer h4{font-size:12px;color:var(--white);font-weight:700;margin-bottom:14px}
.footer ul{list-style:none;font-size:9px;line-height:2.3}
.footer .logo .name,.footer .logo .sub{color:var(--white)}
.f-col{top:3212px}
.signup{display:flex;margin-top:4px}
.signup .in{width:160px;height:26px;background:#2e3337;font-size:9px;padding:6px 8px}
.signup .go{width:26px;height:26px;background:var(--green)}
.copy{left:0;top:3432px;width:1200px;height:36px;background:var(--darker);text-align:center;font-size:9px;color:#8a9096;padding-top:11px}
</style>
</head>
<body>

<div class="abs topbar">CALL US : (800) 555-0142</div>
<header class="abs header">
  <div class="abs logo"><div class="mark"></div><div><span class="name">VELDRAN</span><span class="sub">CONSULTING</span></div></div>
  <nav class="abs nav">
    <a class="active">HOME</a><a>ABOUT US</a><a>TEAM</a><a>PORTFOLIO</a><a>SERVICE</a><a>BLOG</a><a>NEWS</a><a>CONTACT US</a>
  </nav>
</header>

<div class="abs hero" role="img" aria-label="Photo of two colleagues working together in a bright office"></div>
<div class="abs hero-shade"></div>
<div class="abs hero-kicker">BOOST UP YOUR</div>
<h1 class="abs hero-title">LOCAL BUSINESS</h1>
<a class="abs btn hero-btn">CONTACT US</a>
<div class="abs newsletter">
  <div class="nl-label"><div class="nl-icon"></div><div><small>SIGN UP FOR</small>NEWSLETTER</div></div>
  <div class="nl-input">Your name</div>
  <div class="nl-input">Email address</div>
  <div class="nl-btn">SUBSCRIBE NOW</div>
</div>

<div class="abs sec-head" style="top:702px"><span class="tag">WHO</span><h2>WE ARE?</h2></div>
<div class="abs about-img" role="img" aria-label="Photo of consultants reviewing documents at a desk"></div>
<p class="abs about-text">We are a healthcare consultancy helping ministries of health and pharmaceutical companies improve access to medicines around the globe. We work on better healthcare delivery, fair and sustainable pricing, and the practical challenges of emerging markets. Our team brings years of field experience across Latin America, the Middle East, Eastern Europe and Asia, turning complex policy questions into clear plans that reach patients faster.</p>
<a class="abs btn about-btn">READ MORE</a>

<div class="abs services"></div>
<div class="abs sec-head" style="top:1180px"><span class="tag">OUR</span><h2>SERVICES</h2></div>
<div class="abs svc" style="left:180px;top:1250px"><div class="ic on"><svg width="20" height="20"><rect x="2" y="3" width="16" height="14" fill="none" stroke="#fff" stroke-width="2"/><line x1="2" y1="8" x2="18" y2="8" stroke="#fff" stroke-width="2"/></svg></div><div><h4>Data Entry</h4><p>Clean data for pricing and market access decisions.</p></div></div>
<div class="abs svc" style="left:490px;top:1250px"><div class="ic"><svg width="20" height="20"><circle cx="10" cy="7" r="4" fill="none" stroke="#0b6b3a" stroke-width="2"/><path d="M3 18c1-5 13-5 14 0" fill="none" stroke="#0b6b3a" stroke-width="2"/></svg></div><div><h4>Client Management</h4><p>Close partnership with public and private clients.</p></div></div>
<div class="abs svc" style="left:780px;top:1250px"><div class="ic"><svg width="20" height="20"><circle cx="10" cy="4" r="2.5" fill="#0b6b3a"/><circle cx="4" cy="16" r="2.5" fill="#0b6b3a"/><circle cx="16" cy="16" r="2.5" fill="#0b6b3a"/><path d="M10 6v5M10 11L4 14M10 11l6 3" stroke="#0b6b3a" stroke-width="1.5" fill="none"/></svg></div><div><h4>Better Communication</h4><p>Clear dialogue between payers, makers and patients.</p></div></div>
<div class="abs svc" style="left:180px;top:1350px"><div class="ic"><svg width="20" height="20"><rect x="2" y="4" width="16" height="12" fill="none" stroke="#0b6b3a" stroke-width="2"/><line x1="6" y1="8" x2="14" y2="8" stroke="#0b6b3a" stroke-width="2"/><line x1="6" y1="12" x2="12" y2="12" stroke="#0b6b3a" stroke-width="2"/></svg></div><div><h4>Work Analyzing Team</h4><p>Analysts who study delivery gaps and fix them.</p></div></div>
<div class="abs svc" style="left:490px;top:1350px"><div class="ic"><svg width="20" height="20"><path d="M5 3l3 4-2 2c1 2 3 4 5 5l2-2 4 3-2 3C9 18 2 11 2 5z" fill="none" stroke="#0b6b3a" stroke-width="1.6"/></svg></div><div><h4>24 Hour Support</h4><p>Always ready when your programme needs answers.</p></div></div>
<div class="abs svc" style="left:780px;top:1350px"><div class="ic"><svg width="20" height="20"><polyline points="2,16 7,10 11,13 18,4" fill="none" stroke="#0b6b3a" stroke-width="2"/></svg></div><div><h4>Keeping Business Data</h4><p>Secure records that support long-term planning.</p></div></div>

<div class="abs clients"></div>
<div class="abs sec-head light" style="top:1594px"><span class="tag">OUR</span><h2>CLIENTS</h2></div>
<div class="abs quote-ic"></div>
<p class="abs quote">“ Working with this team changed how our ministry plans medicine supply. They understood local constraints, spoke plainly, and gave us a pricing model we could defend and put into action within months. ”</p>
<div class="abs by">by<b>MARLO PENNICK</b></div>
<div class="abs avatar" role="img" aria-label="Client portrait"></div>
<div class="abs dots"><span class="on"></span><span></span><span></span><span></span><span></span></div>

<div class="abs team"></div>
<div class="abs sec-head" style="top:2050px"><span class="tag">OUR</span><h2>TEAM</h2></div>
<div class="abs member" style="left:180px"><div class="photo" role="img" aria-label="Team member portrait"></div><div class="cap"><b>MR. ANDREW LOMAS</b><span>Senior Advisor</span></div></div>
<div class="abs member featured" style="left:392px"><div class="photo" role="img" aria-label="Team member portrait"></div><div class="cap"><b>MICHAEL ROYDEN</b><span>Pricing Expert</span></div></div>
<div class="abs member" style="left:604px"><div class="photo" role="img" aria-label="Team member portrait"></div><div class="cap"><b>MR. DAVID FERRAND</b><span>Market Access Lead</span></div></div>
<div class="abs member" style="left:816px"><div class="photo" role="img" aria-label="Team member portrait"></div><div class="cap"><b>GEORGE MARAL</b><span>Policy Consultant</span></div></div>

<div class="abs sec-head" style="top:2536px"><span class="tag">OUR</span><h2>BLOG POST</h2></div>
<div class="abs blog-img" role="img" aria-label="Photo of hands writing notes during a meeting"></div>
<div class="abs date"><b>15</b><span>DEC</span></div>
<h3 class="abs blog-title">Blog Heading Here</h3>
<div class="abs blog-meta"><span>BY ADMIN</span><span>3 COMMENTS</span></div>
<p class="abs blog-text">Fair medicine prices depend on good data and honest dialogue. In this post we look at how health ministries in emerging markets can work with manufacturers to set prices that protect budgets and keep supply steady, with lessons from recent projects in Latin America and Eastern Europe that show what works in practice.</p>
<a class="abs btn blog-btn">VIEW ALL</a>

<footer class="abs footer"></footer>
<div class="abs logo" style="left:180px;top:3222px"><div class="mark"></div><div><span class="name" style="color:#fff">VELDRAN</span><span class="sub" style="color:#fff">CONSULTING</span></div></div>
<div class="abs f-col" style="left:360px;color:#a8adb2"><h4 style="color:#fff;font-size:12px;margin-bottom:14px">Menu</h4><ul style="list-style:none;font-size:9px;line-height:2.3"><li>HOME</li><li>ABOUT US</li><li>TEAM</li><li>PORTFOLIO</li></ul></div>
<div class="abs f-col" style="left:480px;top:3244px;color:#a8adb2"><ul style="list-style:none;font-size:9px;line-height:2.3"><li>SERVICE</li><li>BLOG</li><li>NEWS</li><li>CONTACT US</li></ul></div>
<div class="abs f-col" style="left:600px;color:#a8adb2"><h4 style="color:#fff;font-size:12px;margin-bottom:14px">Contact</h4><ul style="list-style:none;font-size:9px;line-height:2.3"><li>ADDRESS : 48 Harlow Street, Suite 200</li><li>CONTACT US : (800) 555-0142</li><li>EMAIL : info@veldran.example</li><li>FAX : (800) 555-0143</li></ul></div>
<div class="abs f-col" style="left:860px;color:#a8adb2"><h4 style="color:#fff;font-size:12px;margin-bottom:14px">SIGN UP YOUR NEWSLETTER</h4><div class="signup"><div class="in">Email Address</div><div class="go"></div></div></div>
<div class="abs copy">© 2017 Veldran Consulting. All rights reserved.</div>

</body>
</html>
```